Tavrin Foods Packing 5 to Drive

5 Principals for all the team to follow by!

Please can you convert the 5 to drive "screenshot 2024-09-08" image into something that has a similair look and feel to the Vision and Values style?

```html
<!DOCTYPE html>
<html lang="en">
<head>
<meta charset="utf-8">
<title>Tavrin Foods Packing – 5 Principals</title>
<link href="https://fonts.googleapis.com/css2?family=Montserrat:wght@500;700;800&display=swap" rel="stylesheet">
<style>
  :root{
    --green:#5bb947;
    --red:#d92b2b;
    --panel:#ffffff;
    --night:#161a22;
    --night-2:#20252f;
    --yellow:#d4bd4f;
    --teal:#4f9fab;
    --orange:#d05a2b;
    --crimson:#c3242a;
    --navy:#232638;
    --bar:#a9c8d8;
    --bar-light:#d0dde4;
    --tab:#9fc3d8;
    --ink:#1c2b4e;
    --white:#ffffff;
  }
  *{margin:0;padding:0;box-sizing:border-box}
  html,body{width:1200px;height:800px;overflow:hidden}
  body{font-family:"Montserrat",Arial,sans-serif;background:var(--night)}
  .poster{position:relative;width:1200px;height:800px;
    background:radial-gradient(ellipse at 70% 40%,var(--night-2),var(--night) 70%);}
  .brand-panel{position:absolute;left:0;top:0;width:249px;height:800px;background:var(--panel);
    display:flex;flex-direction:column;align-items:center;justify-content:center;gap:18px;padding:0 20px}
  .brand-dot{width:34px;height:34px;border-radius:50%;background:var(--green)}
  .brand-name{color:var(--green);font-weight:800;font-size:38px;line-height:1.15;text-align:center}
  .title{position:absolute;left:308px;top:34px;width:836px;text-align:center;color:var(--green);
    font-weight:800;font-size:118px;line-height:1;letter-spacing:-1px;white-space:nowrap}
  .subtitle{position:absolute;left:307px;top:149px;width:835px;height:72px;background:var(--red);
    color:var(--white);font-weight:800;font-size:42px;display:flex;align-items:center;justify-content:center;
    letter-spacing:0.5px;white-space:nowrap}
  .principles{list-style:none}
  .principle{position:absolute;left:306px;width:836px;height:94px}
  .principle__bar{position:absolute;left:171px;top:0;right:0;height:94px;background:var(--bar);border-radius:0 3px 3px 0}
  .principle__tile{position:absolute;left:21px;top:0;width:151px;height:94px;background:var(--tile)}
  .principle__tile::after{content:"";position:absolute;right:-13px;top:34px;width:26px;height:26px;border-radius:50%;background:var(--tile)}
  .principle__num{position:absolute;left:0;top:15px;width:68px;height:65px;background:var(--tab);color:var(--ink);
    font-weight:800;font-size:26px;display:flex;align-items:center;padding-left:14px;
    clip-path:polygon(0 0,82% 0,100% 50%,82% 100%,0 100%)}
  .principle__icon{position:absolute;left:82px;top:17px;width:60px;height:60px}
  .principle__label{position:absolute;left:206px;top:0;height:94px;display:flex;align-items:center;
    color:var(--white);font-weight:800;font-size:31px;white-space:nowrap}
  .principle__note{position:absolute;left:546px;top:0;right:0;height:94px;background:var(--bar-light);
    border-radius:0 3px 3px 0;display:flex;align-items:center;padding-left:27px;color:var(--ink);
    font-weight:500;font-size:22px;line-height:1.3}
  .principle__note::before{content:"";position:absolute;left:-13px;top:34px;width:26px;height:26px;border-radius:50%;background:var(--bar-light)}
  .principle--hs{top:244px;--tile:var(--yellow)}
  .principle--gmp{top:349px;--tile:var(--teal)}
  .principle--team{top:454px;--tile:var(--orange)}
  .principle--plan{top:559px;--tile:var(--crimson)}
  .principle--process{top:664px;--tile:var(--navy)}
  .principle--process .principle__tile::after{background:#15171f}
</style>
</head>
<body>
<main class="poster">
  <aside class="brand-panel">
    <span class="brand-dot"></span>
    <span class="brand-name">Tavrin Foods Packing</span>
  </aside>

  <h1 class="title">5 PRINCIPALS</h1>
  <p class="subtitle">FOR ALL THE TEAM TO FOLLOW BY!</p>

  <ol class="principles">
    <li class="principle principle--hs">
      <div class="principle__bar"></div>
      <div class="principle__tile"></div>
      <span class="principle__num">01</span>
      <svg class="principle__icon" viewBox="0 0 60 60" fill="none" stroke="#fff" stroke-width="2.2" stroke-linejoin="round">
        <path d="M30 6 L50 13 V30 C50 42 41 50 30 54 C19 50 10 42 10 30 V13 Z"/>
        <path d="M21 30 L28 37 L40 24"/>
      </svg>
      <span class="principle__label">H&amp;S</span>
      <span class="principle__note">Call It Out</span>
    </li>
    <li class="principle principle--gmp">
      <div class="principle__bar"></div>
      <div class="principle__tile"></div>
      <span class="principle__num">02</span>
      <svg class="principle__icon" viewBox="0 0 60 60" fill="none" stroke="#fff" stroke-width="2.2" stroke-linejoin="round">
        <circle cx="30" cy="30" r="24" stroke-dasharray="4 3"/>
        <circle cx="30" cy="30" r="17"/>
        <path d="M22 30 L28 36 L39 24"/>
      </svg>
      <span class="principle__label">GMP / Quality</span>
      <span class="principle__note">Drive the Standard</span>
    </li>
    <li class="principle principle--team">
      <div class="principle__bar"></div>
      <div class="principle__tile"></div>
      <span class="principle__num">03</span>
      <svg class="principle__icon" viewBox="0 0 60 60" role="img" aria-label="Team icon">
        <rect x="6" y="10" width="48" height="40" rx="20" fill="rgba(255,255,255,0.22)"/>
      </svg>
      <span class="principle__label">Team &amp; Behaviors</span>
      <span class="principle__note">What’s Expected of<br>You and Your Team?</span>
    </li>
    <li class="principle principle--plan">
      <div class="principle__bar"></div>
      <div class="principle__tile"></div>
      <span class="principle__num">04</span>
      <svg class="principle__icon" viewBox="0 0 60 60" fill="none" stroke="#fff" stroke-width="2.2" stroke-linejoin="round">
        <rect x="8" y="42" width="6" height="10"/>
        <rect x="18" y="36" width="6" height="16"/>
        <rect x="28" y="30" width="6" height="22"/>
        <rect x="38" y="24" width="6" height="28"/>
        <rect x="48" y="16" width="6" height="36"/>
        <path d="M8 34 L22 24 L30 28 L50 8 M42 8 H50 V16"/>
      </svg>
      <span class="principle__label">Plan Attainment</span>
    </li>
    <li class="principle principle--process">
      <div class="principle__bar"></div>
      <div class="principle__tile"></div>
      <span class="principle__num">05</span>
      <svg class="principle__icon" viewBox="0 0 60 60" fill="none" stroke="#fff" stroke-width="2.2">
        <path d="M30 6 A24 24 0 0 1 54 30 M54 30 L50 25 M54 30 L57 25"/>
        <path d="M30 54 A24 24 0 0 1 6 30 M6 30 L10 35 M6 30 L3 35"/>
        <circle cx="30" cy="30" r="11" stroke-dasharray="5 2.5" stroke-width="4"/>
        <circle cx="30" cy="30" r="4"/>
      </svg>
      <span class="principle__label">Process Control</span>
    </li>
  </ol>
</main>
</body>
</html>
```